Business card and stationary
Business card and stationary for medical office
Bright & Fun-filled
Gregory L. Hollis, MD
2846 Orwen Ln, Suite B
Lindale, TX 75829
hcplindale@mailpost.example
www.korvafamilypractice.example
logo images uploaded - please feel free to crop out the main logo. Also, on the card somewhere needs the statement, "a KOFP Clinic"
Appointment card and logo
Master logo - I eould encourage you to use the circle logo in creative and unique ways. Please add the tagline, "a KOFP clinic" under the "Hollis Care Partners"

```html
<!DOCTYPE html>
<html lang="en">
<head>
<meta charset="utf-8">
<title>Hollis Care Partners — Stationery Set</title>
<link rel="stylesheet" href="https://fonts.googleapis.com/css2?family=Marcellus&family=Open+Sans:wght@400;600&display=swap">
<style>
  :root {
    --brand-blue: #2f4f95;
    --brand-blue-dark: #243f7c;
    --brand-grey: #9aa0a8;
    --text-grey: #6b7079;
    --paper: #ffffff;
    --stage: #ffffff;
    --rule: #d7dadf;
    --faint: #eceef2;
  }
  * { box-sizing: border-box; margin: 0; padding: 0; }
  html, body { width: 1200px; height: 936px; overflow: hidden; background: var(--stage); }
  .canvas { position: relative; width: 1200px; height: 936px; font-family: "Open Sans", sans-serif; color: var(--text-grey); }
  .sheet { position: absolute; background: var(--paper); border: 1px solid #e3e5e9; overflow: hidden; }

  .brand { display: flex; align-items: center; gap: 10px; }
  .brand-dot { border-radius: 50%; background: var(--brand-blue); flex: none; }
  .brand-name { font-family: "Marcellus", serif; color: var(--brand-blue); text-transform: uppercase; line-height: 1.05; letter-spacing: 0.04em; }
  .brand-tag { font-family: "Marcellus", serif; color: var(--brand-blue); letter-spacing: 0.08em; }

  /* Letterhead */
  .letterhead { left: 185px; top: 63px; width: 393px; height: 548px; }
  .letterhead .edge { position: absolute; left: 0; top: 0; width: 15px; height: 100%; background: var(--brand-blue); }
  .letterhead .edge-rule { position: absolute; left: 19px; top: 0; width: 3px; height: 100%; background: var(--rule); }
  .letterhead .brand { position: absolute; left: 34px; top: 30px; }
  .letterhead .brand-dot { width: 30px; height: 30px; }
  .letterhead .brand-name { font-size: 13px; }
  .contact-list { position: absolute; left: 240px; top: 26px; list-style: none; font-size: 7.5px; line-height: 15px; }
  .contact-list li { display: flex; align-items: center; gap: 5px; }
  .contact-list .bullet { width: 8px; height: 8px; border-radius: 50%; background: var(--brand-blue); flex: none; }
  .watermark-disc { position: absolute; left: 230px; top: 265px; width: 140px; height: 140px; border-radius: 50%; background: var(--faint); }

  /* Folder */
  .folder { left: 634px; top: 46px; width: 503px; height: 565px; }
  .folder .brand { position: absolute; left: 110px; top: 180px; gap: 16px; }
  .folder .brand-dot { width: 66px; height: 66px; }
  .folder .brand-name { font-size: 30px; }
  .folder .brand-tag { font-size: 13px; margin-top: 4px; }
  .folder .rule { position: absolute; left: 0; right: 0; bottom: 38px; height: 3px; background: var(--rule); }
  .folder .band { position: absolute; left: 0; right: 0; bottom: 0; height: 33px; background: var(--brand-blue); color: #fff; font-size: 11px; font-weight: 600; letter-spacing: 0.12em; display: flex; align-items: center; justify-content: center; }

  /* Business cards */
  .card-front { left: 46px; top: 665px; width: 188px; height: 122px; border-radius: 4px; }
  .card-front .edge { position: absolute; left: 0; top: 0; width: 10px; height: 100%; background: var(--brand-blue); }
  .card-front .brand { position: absolute; left: 18px; top: 10px; gap: 5px; }
  .card-front .brand-dot { width: 16px; height: 16px; }
  .card-front .brand-name { font-size: 7px; }
  .card-front .details { position: absolute; left: 18px; top: 46px; font-size: 5.5px; line-height: 9px; }
  .card-front .details-right { position: absolute; right: 10px; top: 64px; font-size: 5.5px; text-align: right; }
  .card-back { left: 46px; top: 807px; width: 188px; height: 111px; border-radius: 8px; background: var(--brand-blue); border: none; }
  .card-back .disc { position: absolute; left: -20px; top: 8px; width: 95px; height: 95px; border-radius: 50%; background: var(--brand-blue-dark); }
  .card-back .url { position: absolute; left: 60px; bottom: 12px; font-size: 6px; color: #fff; letter-spacing: 0.05em; }

  /* Envelopes */
  .envelope-front { left: 261px; top: 667px; width: 437px; height: 213px; }
  .envelope-front .edge { position: absolute; left: 0; top: 0; width: 12px; height: 100%; background: var(--brand-blue); }
  .envelope-front .edge-rule { position: absolute; left: 15px; top: 0; width: 3px; height: 100%; background: var(--rule); }
  .envelope-front .brand { position: absolute; left: 28px; top: 14px; gap: 6px; }
  .envelope-front .brand-dot { width: 24px; height: 24px; }
  .envelope-front .brand-name { font-size: 10px; }
  .envelope-front .return { position: absolute; left: 30px; top: 64px; font-size: 6px; }
  .envelope-back { left: 736px; top: 667px; width: 398px; height: 213px; }
  .envelope-back svg { position: absolute; left: 0; top: 0; }
  .envelope-back .url { position: absolute; left: 0; right: 0; top: 28px; text-align: center; font-size: 8px; color: #fff; letter-spacing: 0.12em; }
</style>
</head>
<body>
<main class="canvas">

  <section class="sheet letterhead" aria-label="Letterhead">
    <div class="edge"></div><div class="edge-rule"></div>
    <div class="brand"><span class="brand-dot"></span><div class="brand-name">Hollis Care<br>Partners</div></div>
    <ul class="contact-list">
      <li><span class="bullet"></span>2846 Orwen Ln, Suite B</li>
      <li><span class="bullet"></span>Lindale, TX 75829</li>
      <li><span class="bullet"></span>Tel 903-555-0148</li>
      <li><span class="bullet"></span>Fax 903-555-0149</li>
      <li><span class="bullet"></span>hcplindale@mailpost.example</li>
      <li><span class="bullet"></span>www.korvafamilypractice.example</li>
    </ul>
    <div class="watermark-disc"></div>
  </section>

  <section class="sheet folder" aria-label="Presentation folder">
    <div class="brand">
      <span class="brand-dot"></span>
      <div><div class="brand-name">Hollis Care<br>Partners</div><div class="brand-tag">a KOFP clinic</div></div>
    </div>
    <div class="rule"></div>
    <div class="band">www.korvafamilypractice.example</div>
  </section>

  <section class="sheet card-front" aria-label="Business card front">
    <div class="edge"></div>
    <div class="brand"><span class="brand-dot"></span><div class="brand-name">Hollis Care<br>Partners</div></div>
    <div class="details">Gregory L. Hollis, MD<br>2846 Orwen Ln, Suite B<br>hcplindale@mailpost.example<br>a KOFP Clinic</div>
    <div class="details-right">Lindale, TX 75829</div>
  </section>

  <section class="sheet card-back" aria-label="Business card back">
    <div class="disc"></div>
    <div class="url">www.korvafamilypractice.example</div>
  </section>

  <section class="sheet envelope-front" aria-label="Envelope front">
    <div class="edge"></div><div class="edge-rule"></div>
    <div class="brand"><span class="brand-dot"></span><div class="brand-name">Hollis Care<br>Partners</div></div>
    <div class="return">2846 Orwen Ln, Suite B, Lindale, TX 75829</div>
  </section>

  <section class="sheet envelope-back" aria-label="Envelope back">
    <svg width="398" height="213" viewBox="0 0 398 213">
      <polygon points="0,0 398,0 398,36 199,92 0,36" fill="var(--brand-blue)"/>
      <line x1="0" y1="213" x2="170" y2="110" stroke="var(--rule)" stroke-width="1"/>
      <line x1="398" y1="213" x2="228" y2="110" stroke="var(--rule)" stroke-width="1"/>
    </svg>
    <div class="url">www.korvafamilypractice.example</div>
  </section>

</main>
</body>
</html>
```